Rollup Banner & Flyer für eine Messe "Erfolg durch Innovation"

Wir benötigten für eine Messe einen Roll Up Banner und Flyer zum verteilen. Gerne basierend auf der aktuellen Firmenpräsentation und mit unseren Referenzen.
Im flyer sollen unserer Leistungen (Datenanalyse, Simulation, Optimierung und Webapplikation) dargestellt werden mit einem kleinen Text und einem aussagekräftigen bild. (https://www.kalvento.ch/leistungen/)

Target Market(s)

Industrie

Industry/Entity Type

Simulation

Font styles to use
Sans Serif
Other font styles liked:
• Roboto

Requirements
Must have
• Logo, Referenzen

```html
<!DOCTYPE html>
<html lang="de">
<head>
<meta charset="utf-8">
<title>Kalvento Roll-up</title>
<link rel="stylesheet" href="https://fonts.googleapis.com/css2?family=Poppins:wght@500;600;700&display=swap">
<style>
:root{
  --accent:#cdd63f;
  --accent-soft:#e4e99a;
  --ink:#111111;
  --paper:#ffffff;
  --stage:#d4d4d4;
  --rule:#dcdcdc;
}
*{margin:0;padding:0;box-sizing:border-box}
html,body{width:1200px;height:701px;overflow:hidden;background:var(--stage)}
.stage{position:relative;width:1200px;height:701px}
.rollup{
  position:absolute;left:465px;top:11px;
  width:462px;height:1160px;background:var(--paper);
  transform:scale(0.586);transform-origin:0 0;
  font-family:"Poppins",sans-serif;color:var(--ink);overflow:hidden;
  box-shadow:0 2px 10px rgba(0,0,0,.12);
}
.top-swoosh{position:absolute;left:0;top:0}
.headline{position:absolute;left:33px;top:52px;font-size:28.5px;font-weight:700;line-height:1.18;letter-spacing:-.2px}
.monitor{position:absolute;left:258px;top:26px;width:171px;height:128px;border:5px solid #1c1c1c;border-radius:3px;background:linear-gradient(180deg,#f4f6fb,#dfe5f2)}
.monitor-stand{position:absolute;left:320px;top:154px;width:48px;height:36px;background:linear-gradient(180deg,#d9d9d9,#b7b7b7);clip-path:polygon(25% 0,75% 0,85% 85%,100% 100%,0 100%,15% 85%)}
.intro{position:absolute;left:33px;top:208px;width:390px;font-size:14.4px;font-weight:500;line-height:1.48;text-align:justify}
.services-box{position:absolute;left:32px;top:309px;width:399px;height:219px;background:var(--ink);border-radius:8px;padding:10px 16px;color:var(--paper)}
.services-box h2{color:var(--accent);font-size:23px;font-weight:700;line-height:1.3}
.services-box p{font-size:14px;font-weight:600;line-height:1.16;text-align:justify;margin-top:2px}
.services-box p + p{margin-top:16px}
.service{position:absolute;left:40px;width:382px;display:flex;gap:12px}
.service-photo{width:104px;height:104px;flex:none;background:linear-gradient(135deg,#3b4a5c,#9fb2c6 60%,#e7edf3)}
.service h3{color:var(--accent);font-size:26px;font-weight:700;line-height:1.1;margin-top:-2px}
.service p{font-size:10.4px;font-weight:600;line-height:1.27;text-align:justify;margin-top:3px}
.service-rule{position:absolute;left:40px;width:382px;height:1px;background:var(--rule)}
.brand{position:absolute;left:40px;top:1053px;display:flex;align-items:center;gap:10px}
.brand-dot{width:44px;height:44px;border-radius:50%;background:var(--ink)}
.brand-name{font-size:34px;font-weight:600;color:var(--ink);letter-spacing:.5px}
.badge{position:absolute;left:305px;top:1027px;width:118px;height:118px;border-radius:50%;border:7px solid var(--accent);background:#fff;padding:6px}
.badge-photo{width:100%;height:100%;border-radius:50%;background:radial-gradient(circle at 40% 35%,#cfd6de,#6f7a86 70%,#2f353d)}
.bottom-band{position:absolute;left:0;bottom:0}
</style>
</head>
<body>
<div class="stage">
  <div class="rollup">
    <svg class="top-swoosh" width="462" height="40" viewBox="0 0 462 40" aria-hidden="true">
      <path d="M190 0 H462 V28 C380 8 290 4 190 0Z" fill="var(--accent-soft)"/>
      <path d="M300 0 H462 V18 C410 6 350 2 300 0Z" fill="var(--accent)"/>
    </svg>

    <h1 class="headline">Du Hast Eine<br>Schwierige<br>Entscheidung<br>Zu Treffen?</h1>
    <div class="monitor" role="img" aria-label="Bildschirm mit Dashboard und Balkendiagrammen"></div>
    <div class="monitor-stand" aria-hidden="true"></div>

    <p class="intro">Was wäre, wenn wir dir zeigen würden, welche Option die Beste ist? Wir unterstützen Unternehmen in Logistik und Produktion die besten Entscheidungen zu treffen und dass innerhalb weniger Wochen.</p>

    <section class="services-box">
      <h2>Leistungen</h2>
      <p>Mit Simulation, Datenanalyse und Optimierung entwickeln wir Lösungen, die komplexe Prozesse sichtbar machen, Varianten vergleichbar machen und bessere Entscheidungen ermöglichen.</p>
      <p>Wir begleiten unsere Kunden vom schnellen Vorprojekt bis zur produktiven Lösung – pragmatisch, technisch stark und immer mit Fokus auf dem Nutzen.</p>
    </section>

    <article class="service" style="top:550px">
      <div class="service-photo" role="img" aria-label="Foto: Präsentation von Datenanalysen in einem Besprechungsraum"></div>
      <div><h3>Datenanalyse</h3><p>Datenanalyse macht Prozesse sichtbar, erkennt Muster und schafft eine objektive Grundlage für Entscheidungen. Wir strukturieren, bereinigen und analysieren Daten so, dass sie einen echten Nutzen erzeugen.</p></div>
    </article>
    <div class="service-rule" style="top:660px"></div>

    <article class="service" style="top:667px">
      <div class="service-photo" style="background:linear-gradient(135deg,#e9eef3,#b9c6d3 60%,#7f8fa0)" role="img" aria-label="Foto: Hände vor Bildschirm mit Diagrammen"></div>
      <div><h3>Simulation</h3><p>Simulation bildet reale Prozesse digital ab, damit Abläufe, Kapazitäten und Varianten risikofrei getestet werden können.</p></div>
    </article>
    <div class="service-rule" style="top:777px"></div>

    <article class="service" style="top:784px">
      <div class="service-photo" style="background:linear-gradient(135deg,#5a4a3c,#a9a195 55%,#dfe3e6)" role="img" aria-label="Foto: Tablet mit Auswertungen auf einem Tisch"></div>
      <div><h3>Optimierung</h3><p>Optimierung sucht automatisch nach der besten Lösung – sei es bei Planung, Ressourcen, Routen oder Abläufen. Mit Algorithmen und intelligenten Modellen finden wir Varianten, die Kosten senken, Kapazitäten besser nutzen und Entscheidungen beschleunigen.</p></div>
    </article>
    <div class="service-rule" style="top:898px"></div>

    <article class="service" style="top:906px">
      <div class="service-photo" style="background:linear-gradient(135deg,#2c4763,#8fa9c4 55%,#eef1f4)" role="img" aria-label="Foto: Arbeitsplatz mit Monitor und Webanwendung"></div>
      <div><h3>Webapplikationen</h3><p>Wir entwickeln individuelle Webapplikationen, die Daten, Simulationen und Optimierungen in einem benutzerfreundlichen Tool zusammenführen. So entstehen Lösungen, die direkt im Alltag genutzt werden – einfach, schnell und ohne Installation.</p></div>
    </article>

    <div class="brand">
      <span class="brand-dot" aria-hidden="true"></span>
      <span class="brand-name">Kalvento</span>
    </div>

    <svg class="bottom-band" width="462" height="40" viewBox="0 0 462 40" aria-hidden="true">
      <rect x="0" y="0" width="462" height="40" fill="var(--accent)"/>
      <path d="M212 40 C240 20 255 6 290 4 H462 V40Z" fill="var(--ink)"/>
    </svg>

    <div class="badge"><div class="badge-photo" role="img" aria-label="Foto: Hand zieht eine Schachfigur auf dem Brett"></div></div>
  </div>
</div>
</body>
</html>
```